Urine collection cup with and without sterile seal sticker

Hello. We need a urine cup label designed please with

Name:
Date of Birth:
Date:
Time:
Temp℃:
Specimen ID:

Product code: TUB-47
Volume markings (e.g., 30 mL, 60 mL, 90 mL).
Vela Drug Tests logo

Could you please provide one version with the additional sterile sticker extending to the top, and one version without the additional sterile sticker?

```html
<!DOCTYPE html>
<html lang="en">
<head>
<meta charset="UTF-8">
<title>Vela Drug Tests – Urine Collection Container Label</title>
<link rel="stylesheet" href="https://fonts.googleapis.com/css2?family=Roboto+Condensed:wght@700&family=Roboto:wght@700&display=swap">
<style>
  :root {
    --page-bg: #f1fefe;
    --label-white: #ffffff;
    --ink-navy: #0d1e36;
    --accent-blue: #2a9fe8;
    --rule-grey: #1c2838;
    --rule-light: #8d97a3;
    --icon-dark: #1b2430;
    --icon-grey: #8d97a3;
    --icon-pale: #a9b1ba;
  }
  * { margin: 0; padding: 0; box-sizing: border-box; }
  html, body {
    width: 907px; height: 1200px; overflow: hidden;
    background: var(--page-bg);
  }
  .stage { position: relative; width: 907px; height: 1200px; }

  .label {
    position: absolute; left: 181px; top: 423px;
    width: 525px; height: 354px;
    background: var(--label-white);
    box-shadow: 0 6px 22px rgba(40, 60, 70, 0.28);
    font-family: "Roboto Condensed", "Arial Narrow", sans-serif;
    font-weight: 700;
    color: var(--ink-navy);
  }

  .field-name {
    position: absolute; font-size: 23px; line-height: 1;
    transform: translateY(-80%);
    white-space: nowrap;
  }
  .field-name sup { font-size: 12px; vertical-align: 9px; line-height: 0; }
  .field-rule { position: absolute; height: 1px; background: var(--rule-grey); }

  .specimen-pill {
    position: absolute; left: 44px; top: 204px;
    width: 434px; height: 44px;
    border: 1px solid var(--ink-navy); border-radius: 22px;
    background: var(--label-white); overflow: hidden;
  }
  .specimen-tag {
    position: absolute; left: 0; top: 0; bottom: 0; width: 155px;
    background: var(--ink-navy);
    border-radius: 22px;
    color: var(--accent-blue); font-size: 24px; line-height: 1;
    display: flex; align-items: center; padding-left: 13px;
    white-space: nowrap;
  }

  .footer-band {
    position: absolute; left: 0; right: 0; bottom: 0; height: 89px;
    background: var(--ink-navy);
  }
  .brand {
    position: absolute; left: 44px; top: 12px;
    display: flex; align-items: center; gap: 6px;
  }
  .brand-dot {
    width: 30px; height: 30px; border-radius: 50%;
    background: var(--accent-blue);
  }
  .brand-name {
    color: var(--label-white); font-size: 26px; line-height: 1;
    white-space: nowrap;
  }
  .test-icons { position: absolute; left: 382px; top: 19px; }
  .product-line {
    position: absolute; left: 44px; top: 53px;
    font-family: "Roboto", Arial, sans-serif; font-size: 12.5px; line-height: 14px;
    letter-spacing: 1.7px; color: var(--label-white);
    white-space: nowrap;
  }
  .product-rule {
    position: absolute; left: 279px; top: 64px; width: 151px; height: 1px;
    background: var(--rule-light);
  }
  .volume {
    position: absolute; right: 58px; top: 53px;
    font-family: "Roboto", Arial, sans-serif; font-size: 12.5px; line-height: 14px;
    color: var(--accent-blue);
  }
</style>
</head>
<body>
<main class="stage">
  <section class="label" aria-label="Urine collection container label">
    <span class="field-name" style="left:43px; top:74px;">Name:</span>
    <span class="field-rule" style="left:111px; top:73px; width:365px;"></span>

    <span class="field-name" style="left:43px; top:124px;">DOB:</span>
    <span class="field-rule" style="left:95px; top:123px; width:182px;"></span>
    <span class="field-name" style="left:287px; top:124px;">Date:</span>
    <span class="field-rule" style="left:343px; top:123px; width:133px;"></span>

    <span class="field-name" style="left:43px; top:174px;">Temp<sup>0</sup>C:</span>
    <span class="field-rule" style="left:126px; top:174px; width:151px;"></span>
    <span class="field-name" style="left:287px; top:175px;">Time:</span>
    <span class="field-rule" style="left:343px; top:174px; width:133px;"></span>

    <div class="specimen-pill">
      <div class="specimen-tag">Specimen ID</div>
    </div>

    <footer class="footer-band">
      <div class="brand">
        <span class="brand-dot"></span>
        <span class="brand-name">Vela Drug Tests</span>
      </div>
      <svg class="test-icons" width="88" height="26" viewBox="0 0 88 26" role="img" aria-label="Drug class icons: bottle, syringe, cannabis, alcohol">
        <circle cx="12" cy="13" r="12" fill="var(--icon-dark)"/>
        <circle cx="34" cy="13" r="12" fill="var(--icon-grey)"/>
        <circle cx="54" cy="13" r="12" fill="var(--accent-blue)"/>
        <circle cx="75" cy="13" r="12" fill="var(--icon-pale)"/>
      </svg>
      <span class="product-line">URINE COLLECTION CONTAINER</span>
      <span class="product-rule"></span>
      <span class="volume">90ML</span>
    </footer>
  </section>
</main>
</body>
</html>
```